Velora Crest Label

Design a label for the new brand Velora Crest. The specific product label : Velora Crest Deep Moisturizing Conditioner.

You only need to design the front label.I have included the logo and a bottle jpeg. Please try your best.

Industry/Entity Type

Product

Requirements
Must have
• text you can use:
• For Dry, Damaged Hair
• Strengthening & Moisturizing Conditioner
• Moisture Infused
• Deep Penetrating Formula
• Used by Professionals
• 8.5oz/250ml

```html
<!DOCTYPE html>
<html lang="en">
<head>
<meta charset="utf-8">
<title>Velora Crest Deep Moisturizing Conditioner – Front Label</title>
<link rel="stylesheet" href="https://fonts.googleapis.com/css2?family=Archivo+Black&family=Montserrat:wght@800&display=swap">
<style>
  :root {
    --label-dark: #24170f;
    --gold: #f5b800;
    --gold-deep: #d98e00;
    --gold-light: #ffe36a;
    --cream: #fff8d0;
    --ink-blue: #16238c;
    --badge-red: #d8231c;
    --badge-red-dark: #9e1410;
    --white: #ffffff;
  }
  * { margin: 0; padding: 0; box-sizing: border-box; }
  html, body {
    width: 1200px; height: 2684px; overflow: hidden;
    background: var(--label-dark);
  }
  .label {
    position: relative; width: 1200px; height: 2684px;
    background: var(--label-dark); overflow: hidden;
  }
  .label__waves { position: absolute; inset: 0; width: 1200px; height: 2684px; }

  .badge {
    position: absolute; left: 205px; top: 150px;
    width: 370px; height: 250px;
    transform: rotate(-14deg);
    background: linear-gradient(180deg, var(--badge-red) 0%, var(--badge-red-dark) 100%);
    border: 8px solid var(--gold-light);
    border-radius: 34px;
    display: flex; flex-direction: column; align-items: center; justify-content: center;
    font-family: "Archivo Black", sans-serif; color: var(--white); line-height: 1;
  }
  .badge__new { font-size: 104px; letter-spacing: 2px; }
  .badge__improved { font-size: 70px; color: var(--gold-light); margin-top: 6px; }

  .hair-type {
    position: absolute; right: 70px; top: 420px;
    font-family: "Archivo Black", sans-serif; font-size: 78px; line-height: 1.08;
    color: var(--ink-blue); text-align: right;
  }

  .brand {
    position: absolute; left: 140px; top: 1400px;
    font-family: "Montserrat", sans-serif; font-weight: 800;
    color: var(--gold); line-height: 1;
  }
  .brand__first { display: block; font-size: 170px; letter-spacing: -2px; }
  .brand__second { display: block; font-size: 140px; margin: 10px 0 0 300px; }

  .product-name {
    position: absolute; left: 0; right: 0; top: 2040px;
    font-family: "Archivo Black", sans-serif; font-size: 124px; line-height: 1.05;
    color: var(--ink-blue); text-align: center;
  }

  .volume {
    position: absolute; right: 80px; top: 2520px;
    font-family: "Montserrat", sans-serif; font-weight: 800; font-size: 64px;
    color: var(--white);
  }
</style>
</head>
<body>
<main class="label">
  <svg class="label__waves" viewBox="0 0 1200 2684" aria-hidden="true">
    <defs>
      <linearGradient id="goldBand" x1="0" y1="0" x2="1" y2="1">
        <stop offset="0" stop-color="#ffd21f"/>
        <stop offset="0.5" stop-color="#fff3a8"/>
        <stop offset="1" stop-color="#f5b800"/>
      </linearGradient>
      <linearGradient id="goldBandLow" x1="0" y1="0" x2="0" y2="1">
        <stop offset="0" stop-color="#f5b800"/>
        <stop offset="0.45" stop-color="#fff8d0"/>
        <stop offset="0.75" stop-color="#ffe36a"/>
        <stop offset="1" stop-color="#e39a00"/>
      </linearGradient>
    </defs>
    <!-- top sweep -->
    <path class="wave wave--top-edge" fill="#d98e00"
      d="M0,360 C260,380 560,290 720,140 C790,70 850,25 880,0 L1200,0 L1200,690 C900,660 480,580 0,640 Z"/>
    <path class="wave wave--top" fill="url(#goldBand)"
      d="M0,390 C270,405 580,320 750,160 C820,90 870,35 900,0 L1200,0 L1200,660 C900,630 480,560 0,610 Z"/>
    <!-- bottom sweep -->
    <path class="wave wave--bottom-edge" fill="#d98e00"
      d="M0,1660 C320,1740 720,1880 1200,1930 L1200,2470 C820,2470 400,2540 0,2684 Z"/>
    <path class="wave wave--bottom" fill="url(#goldBandLow)"
      d="M0,1700 C320,1780 720,1910 1200,1960 L1200,2430 C820,2440 400,2510 0,2650 Z"/>
  </svg>

  <div class="badge">
    <span class="badge__new">NEW</span>
    <span class="badge__improved">Improved</span>
  </div>

  <p class="hair-type">For Dry<br>Dameged Hair</p>

  <h1 class="brand">
    <span class="brand__first">Velora</span>
    <span class="brand__second">Crest</span>
  </h1>

  <h2 class="product-name">Deep<br>Moisturizing<br>Conditioner.</h2>

  <p class="volume">8.5oz/250ml</p>
</main>
</body>
</html>
```